Coffee bag stamp design for new coffee brand

Stamp design that will be used like a label on a coffee package.
It must be a vector that can be produced as a stamp. Coffee bag is from brown craft paper. I upload image of this bag. Size of design is 80mm x 140mm.
I also uploaded two pictures for inspiration, but I will also appreciate new ideas.

Target Market(s)

Coffee lovers, who love to try new coffee. Also hipsters.

Colors

Designer to choose only greyscale colors for use in the design.

Requirements
Must have
• Some information about coffee must have:
Name: BRAZIL (the biggest font in that design)
Region: Santos
Altitude: 60 – 1200 m.n.m.
Variety: Arabica
Processing: unwashed

```html
<!DOCTYPE html>
<html lang="en">
<head>
<meta charset="utf-8">
<title>Brazil Santos – Coffee Bag Stamp</title>
<link rel="stylesheet" href="https://fonts.googleapis.com/css2?family=Montserrat:wght@600;700;800;900&display=swap">
<style>
  :root {
    --paper-light: #c2c2c2;
    --paper-dark: #ababab;
    --ink: #0d0d0d;
  }
  * { margin: 0; padding: 0; box-sizing: border-box; }
  html, body {
    width: 1200px;
    height: 800px;
    overflow: hidden;
  }
  body {
    background: linear-gradient(170deg, var(--paper-light), var(--paper-dark));
    font-family: "Montserrat", sans-serif;
  }
  .stamp {
    position: absolute;
    left: 258px;
    top: 80px;
    width: 684px;
    height: 639px;
  }
  .stamp-rule { stroke: var(--ink); stroke-width: 3; }
  .origin-name {
    font-family: "Montserrat", sans-serif;
    font-weight: 900;
    font-size: 168px;
    fill: var(--ink);
  }
  .side-label {
    font-family: "Montserrat", sans-serif;
    font-weight: 800;
    font-size: 26px;
    letter-spacing: 1px;
    fill: var(--ink);
  }
  .brand-name {
    font-family: "Montserrat", sans-serif;
    font-weight: 800;
    fill: var(--ink);
  }
  .brand-dot { fill: var(--ink); }
  .origin-details {
    font-family: "Montserrat", sans-serif;
    font-weight: 700;
    font-size: 50px;
    fill: var(--ink);
  }
</style>
</head>
<body>
  <svg class="stamp" viewBox="340 470 760 710" xmlns="http://www.w3.org/2000/svg" aria-label="Brazil coffee stamp label">
    <defs>
      <path id="origin-arc" d="M405,900 A310,310 0 0 1 1025,900" fill="none"/>
    </defs>

    <text class="origin-name">
      <textPath href="#origin-arc" startOffset="50%" text-anchor="middle" textLength="700" lengthAdjust="spacing">BRAZIL</textPath>
    </text>

    <g class="variety">
      <line class="stamp-rule" x1="343" y1="856" x2="482" y2="856"/>
      <text class="side-label" x="412" y="901" text-anchor="middle">ARABICA</text>
      <line class="stamp-rule" x1="343" y1="928" x2="482" y2="928"/>
    </g>

    <g class="brand">
      <circle class="brand-dot" cx="710" cy="800" r="26"/>
      <text class="brand-name" x="710" y="900" text-anchor="middle" font-size="66">KALMA</text>
      <text class="brand-name" x="710" y="946" text-anchor="middle" font-size="40">COFFEE</text>
    </g>

    <g class="processing">
      <line class="stamp-rule" x1="931" y1="856" x2="1099" y2="856"/>
      <text class="side-label" x="1013" y="901" text-anchor="middle">UNWASHED</text>
      <line class="stamp-rule" x1="931" y1="928" x2="1099" y2="928"/>
    </g>

    <g class="origin">
      <line class="stamp-rule" x1="345" y1="1056" x2="1095" y2="1056"/>
      <text class="origin-details" x="720" y="1122" text-anchor="middle">SANTOS / Alt. 60-120 m.n.m</text>
      <line class="stamp-rule" x1="345" y1="1158" x2="1095" y2="1158"/>
      <line class="stamp-rule" x1="345" y1="1165" x2="1095" y2="1165"/>
    </g>
  </svg>
</body>
</html>
```